Product Sales Website Design - E-commerce - Shopify etc

We have been selling printing equipment for some time now and think that it will be useful to sell the products on the internet, using a simple e-commerce platform, such as shopify etc. There are roughly a few dozen products - so basically, the idea is to have a modern, simple and clean home page. When someone looks at it, they think, this is it - I want to buy here. I am not going to impose any ideas or say how I want it done.

Just so you know, at the moment there are three categories of products. One being printers, scanners and accessories.

I am excited by this whole project and don't want to have good designers backing out because they feel i am imposing restrictions. Feel free to impress me.

Industry/Entity Type

E-Commerce

Requirements
Must have
• integration with an e-commerce platform is a must or show how to integrate, so I can easily introduce further products.

```html
<!DOCTYPE html>
<html lang="en">
<head>
<meta charset="utf-8">
<title>PressPoint — Printers, Scanners &amp; Accessories</title>
<link rel="stylesheet" href="https://fonts.googleapis.com/css2?family=Arimo:wght@400;700&family=Inter:wght@200;300;400&display=swap">
<style>
  :root {
    --ink: #1b1b1b;
    --yellow: #ffd200;
    --yellow-deep: #f6bd00;
    --accent-blue: #0f5aa8;
    --link-blue: #1a5fb4;
    --heading: #111111;
    --body-grey: #7a7a7a;
    --small-grey: #555555;
    --rule: #cfcfcf;
    --dot: #bdbdbd;
    --white: #ffffff;
    --product-dark: #2a2a2a;
    --product-mid: #4a4a4a;
    --paper: #ececec;
  }
  * { margin: 0; padding: 0; box-sizing: border-box; }
  html, body { width: 1200px; height: 760px; overflow: hidden; }
  body {
    position: relative;
    background: var(--white);
    font-family: "Arimo", Arial, sans-serif;
    color: var(--heading);
  }

  /* Header */
  .site-header {
    position: absolute; left: 0; top: 0; width: 1200px; height: 120px;
    background: var(--ink);
    border-top: 4px solid var(--yellow);
  }
  .brand {
    position: absolute; left: 133px; top: 11px;
    display: flex; align-items: center; gap: 6px;
  }
  .brand-mark { width: 50px; height: 48px; background: var(--accent-blue); }
  .brand-name {
    font-family: "Arimo", Arial, sans-serif; font-weight: 700;
    font-size: 34px; color: var(--white); letter-spacing: -0.5px;
  }
  .main-nav {
    position: absolute; right: 139px; top: 28px;
    display: flex; list-style: none;
  }
  .main-nav li {
    font-family: "Inter", Arial, sans-serif; font-weight: 200;
    font-size: 16.5px; letter-spacing: -0.2px; color: var(--white);
    padding: 0 13px; border-left: 1px solid var(--yellow-deep);
    line-height: 23px;
  }
  .main-nav li:first-child { border-left: none; }
  .main-nav li:last-child { padding-right: 0; }
  .category-tabs {
    position: absolute; left: 134px; top: 78px;
    display: flex; gap: 2px; list-style: none;
  }
  .category-tabs li {
    width: 122.5px; height: 38px;
    background: linear-gradient(var(--yellow), var(--yellow-deep));
  }

  /* Hero */
  .hero-title {
    position: absolute; left: 170px; top: 176px;
    font-weight: 700; font-size: 56px; letter-spacing: 1.6px; line-height: 60px;
  }
  .hero-price {
    position: absolute; left: 170px; top: 236px;
    font-family: "Inter", Arial, sans-serif; font-weight: 300;
    font-size: 23px; line-height: 40px; letter-spacing: -0.5px;
  }
  .hero-price strong {
    font-family: "Arimo", Arial, sans-serif; font-weight: 700;
    font-size: 34px; margin-left: 10px; letter-spacing: 0;
  }
  .hero-copy {
    position: absolute; left: 171px; top: 281px;
    font-size: 17px; line-height: 20.5px; color: var(--body-grey);
  }
  .hero-button {
    position: absolute; left: 170px; top: 354px; width: 109px; height: 34px;
    border-radius: 6px;
    background: linear-gradient(var(--yellow), var(--yellow-deep));
  }
  .hero-visual {
    position: absolute; left: 562px; top: 160px; width: 405px; height: 240px;
    background: radial-gradient(ellipse 60% 55% at 45% 55%, #cfcfcf, #e6e6e6 55%, rgba(255,255,255,0) 100%);
  }
  .slider-dots {
    position: absolute; left: 519px; top: 433px;
    display: flex; gap: 29px; list-style: none;
  }
  .slider-dots li { width: 9px; height: 9px; border-radius: 50%; background: var(--dot); }
  .slider-dots li.is-active { background: var(--accent-blue); }
  .section-rule {
    position: absolute; left: 151px; top: 459px; width: 880px; height: 1px;
    background: var(--rule);
  }

  /* Featured products */
  .column-rule {
    position: absolute; top: 477px; width: 1px; height: 128px; background: var(--rule);
  }
  .product-shot {
    position: absolute; border-radius: 3px;
    background: linear-gradient(var(--product-mid), var(--product-dark) 65%, var(--paper));
  }
  .product-card { position: absolute; top: 590px; }
  .product-card h3 {
    font-weight: 400; font-size: 17.4px; color: var(--link-blue); line-height: 22px;
  }
  .product-card p {
    margin-top: 1px; font-size: 12.8px; line-height: 15px; color: var(--small-grey);
  }

  /* Footer */
  .site-footer {
    position: absolute; left: 0; top: 700px; width: 1200px; height: 60px;
    background: var(--ink); border-top: 5px solid var(--yellow);
  }
</style>
</head>
<body>
  <header class="site-header">
    <div class="brand">
      <span class="brand-mark"></span>
      <span class="brand-name">PressPoint</span>
    </div>
    <ul class="main-nav">
      <li>About</li>
      <li>Products</li>
      <li>Order</li>
      <li>Contact</li>
    </ul>
    <ul class="category-tabs">
      <li></li><li></li><li></li><li></li><li></li>
    </ul>
  </header>

  <main>
    <section class="hero">
      <h1 class="hero-title">PRINTERS</h1>
      <p class="hero-price">STARTING AT<strong>$60</strong></p>
      <p class="hero-copy">Lorem ipsum dolor sit amet<br>consectetur adipiscing elit sit amet<br>Dolor amet ipsum lorem.</p>
      <span class="hero-button"></span>
      <div class="hero-visual" role="img" aria-label="Photo group of inkjet printers, an all-in-one printer and a document scanner"></div>
      <ul class="slider-dots">
        <li class="is-active"></li><li></li><li></li><li></li><li></li>
      </ul>
    </section>

    <div class="section-rule"></div>

    <section class="featured">
      <div class="column-rule" style="left:419px"></div>
      <div class="column-rule" style="left:780px"></div>

      <div class="product-shot" style="left:230px;top:494px;width:100px;height:78px" role="img" aria-label="Photo of a black compact inkjet printer"></div>
      <div class="product-shot" style="left:538px;top:507px;width:120px;height:45px" role="img" aria-label="Photo of a slim black photo printer"></div>
      <div class="product-shot" style="left:878px;top:494px;width:82px;height:72px" role="img" aria-label="Photo of a black multifunction laser printer"></div>

      <article class="product-card" style="left:166px">
        <h3>Lorem ipsum dolor sit amet</h3>
        <p>consectetur adipiscing elit sit amet<br>Dolor amet ipsum lorem.</p>
      </article>
      <article class="product-card" style="left:494px">
        <h3>Lorem ipsum dolor sit amet</h3>
        <p>consectetur adipiscing elit sit amet<br>Dolor amet ipsum lorem.</p>
      </article>
      <article class="product-card" style="left:821px">
        <h3>Lorem ipsum dolor sit amet</h3>
        <p>consectetur adipiscing elit sit amet<br>Dolor amet ipsum lorem.</p>
      </article>
    </section>
  </main>

  <footer class="site-footer"></footer>
</body>
</html>
```